Design a Word Template and Powerpoint Template for a Venture Capital Fund

I'm looking to get a powerpoint template and word template designed ASAP under the same selected design. Its for a finance / Venture Capital business... keen to keep it clean but "pop" and stand up on its own as a strong brand, solid templates etc... Happy to talk. Thanks Kit

Target Market(s)

Venture Capital and Private Equity

Industry/Entity Type

Finance / Venture Capital / Management Consulting

Requirements
Nice to have
• Strong formatting, icons and optionality, images can be good too

```html
<!DOCTYPE html>
<html lang="en">
<head>
<meta charset="utf-8">
<title>Northfield Ventures – Presentation Template Overview</title>
<link rel="stylesheet" href="https://fonts.googleapis.com/css2?family=Michroma&family=Montserrat:wght@400;600;700&family=Open+Sans&display=swap">
<style>
:root{
  --ink:#000;
  --paper:#fff;
  --mist:#d6d6d6;
  --fog:#ececec;
  --rule:#c4c4c4;
  --stage:#f2f2f2;
  --label:#4a4a4a;
}
*{box-sizing:border-box;margin:0;padding:0}
html,body{width:1200px;height:567px;overflow:hidden}
body{background:var(--stage);position:relative;font-family:"Montserrat",sans-serif;-webkit-font-smoothing:antialiased;-moz-osx-font-smoothing:grayscale}
.slot{position:absolute;width:162px;height:110px}
.slide{position:absolute;left:0;top:0;width:162px;height:92px;background:var(--paper);color:var(--ink);border:1px solid var(--rule);overflow:hidden}
.slide.dark{background:var(--ink);color:var(--paper)}
.slot-num{position:absolute;left:1px;top:95px;font:13px "Open Sans",sans-serif;color:var(--label)}
.slot-star{position:absolute;right:2px;top:97px;font-size:10px;color:#777}
.abs{position:absolute}
.block-ink{position:absolute;background:var(--ink)}
.block-mist{position:absolute;background:var(--mist)}
.block-paper{position:absolute;background:var(--paper)}
.block-fog{position:absolute;background:var(--fog)}
.heading{position:absolute;font-family:"Michroma",sans-serif;font-size:4px;line-height:1.25;letter-spacing:.12em;text-transform:uppercase;color:inherit}
.heading.center{left:0;right:0;text-align:center}
.heading.ruled{border-left:.5px solid currentColor;padding-left:3px}
.heading-rule{position:absolute;width:7px;height:.6px;background:currentColor}
.fine{position:absolute;font-size:1.9px;line-height:1.45;color:inherit}
.fine b,.fine.bold{font-weight:700}
.lead{position:absolute;font-size:2.3px;line-height:1.4;font-weight:700}
.brand{position:absolute;display:flex;align-items:center;gap:2px;font-family:"Michroma",sans-serif;letter-spacing:.1em;text-transform:uppercase;white-space:nowrap}
.brand-square{display:inline-block;border:.5px solid currentColor}
.footer{position:absolute;left:4px;bottom:3px;display:flex;align-items:center;gap:1.5px;font-family:"Michroma",sans-serif;font-size:1.8px;letter-spacing:.08em;text-transform:uppercase}
.footer i{width:2px;height:2px;background:currentColor;display:inline-block}
.col-divider{position:absolute;width:.5px;background:var(--rule)}
.icon{position:absolute}
.client-box{position:absolute;width:17px;height:5px;border:.5px solid #999;background:var(--fog)}
.photo{position:absolute;background:var(--mist)}
</style>
</head>
<body>

<!-- Row 1 -->
<div class="slot" style="left:25px;top:16px">
  <div class="slide">
    <div class="brand" style="left:56px;top:42px;font-size:4px"><span class="brand-square" style="width:6px;height:6px"></span>Northfield Ventures</div>
  </div>
  <span class="slot-num">1</span><span class="slot-star">★</span>
</div>

<div class="slot" style="left:220px;top:16px">
  <div class="slide dark">
    <div class="brand" style="left:56px;top:42px;font-size:4px"><span class="brand-square" style="width:6px;height:6px"></span>Northfield Ventures</div>
  </div>
  <span class="slot-num">2</span><span class="slot-star">★</span>
</div>

<div class="slot" style="left:414px;top:16px">
  <div class="slide">
    <div class="heading ruled" style="left:62px;top:38px">Presentation<br>Title</div>
    <div class="fine bold" style="left:6px;top:82px">MAY 2024</div>
    <div class="brand" style="left:118px;top:76px;font-size:2px"><span class="brand-square" style="width:4px;height:4px"></span>Northfield</div>
    <div class="fine" style="left:124px;top:80px;width:32px;font-size:1.6px">12 Harbour Lane, Suite 4<br>hello@northfield.vc</div>
  </div>
  <span class="slot-num">3</span>
</div>

<div class="slot" style="left:608px;top:16px">
  <div class="slide dark">
    <div class="heading ruled" style="left:62px;top:38px">Presentation<br>Title</div>
    <div class="fine bold" style="left:6px;top:82px">MAY 2024</div>
    <div class="brand" style="left:118px;top:76px;font-size:2px"><span class="brand-square" style="width:4px;height:4px"></span>Northfield</div>
    <div class="fine" style="left:124px;top:80px;width:32px;font-size:1.6px">12 Harbour Lane, Suite 4<br>hello@northfield.vc</div>
  </div>
  <span class="slot-num">4</span>
</div>

<div class="slot" style="left:803px;top:16px">
  <div class="slide dark">
    <div class="heading ruled" style="left:62px;top:38px">Sectional<br>Heading</div>
  </div>
  <span class="slot-num">5</span>
</div>

<div class="slot" style="left:997px;top:16px">
  <div class="slide">
    <div class="heading ruled" style="left:62px;top:38px">About<br>Us</div>
  </div>
  <span class="slot-num">6</span>
</div>

<!-- Row 2 -->
<div class="slot" style="left:25px;top:156px">
  <div class="slide">
    <div class="heading" style="left:12px;top:10px">About<br>Us</div>
    <div class="heading-rule" style="left:12px;top:23px"></div>
    <div class="photo" style="left:110px;top:0;width:52px;height:64px" role="img" aria-label="Team photograph"></div>
    <div class="block-ink" style="left:124px;top:64px;width:38px;height:28px"></div>
    <div class="lead" style="left:12px;top:44px;width:64px">Capital, counsel and a trusted network built for the very first rounds.</div>
    <div class="fine" style="left:12px;top:53px;width:28px">We back bold founders at the earliest stage, offering capital, counsel and a trusted network. Our partners stay close through every round, helping teams hire, sell and scale with focus and care.</div>
    <div class="fine" style="left:44px;top:53px;width:28px">We back bold founders at the earliest stage, offering capital, counsel and a trusted network. Our partners stay close through every round, helping teams hire, sell and scale with focus and care.</div>
    <div class="footer"><i></i>Northfield Ventures</div>
  </div>
  <span class="slot-num">7</span>
</div>

<div class="slot" style="left:220px;top:156px">
  <div class="slide dark">
    <div class="heading" style="left:12px;top:10px">About<br>Us</div>
    <div class="heading-rule" style="left:12px;top:23px"></div>
    <div class="photo" style="left:112px;top:0;width:50px;height:68px" role="img" aria-label="Team photograph"></div>
    <div class="block-paper" style="left:132px;top:68px;width:30px;height:24px"></div>
    <div class="lead" style="left:12px;top:44px;width:64px">Capital, counsel and a trusted network built for the very first rounds.</div>
    <div class="fine" style="left:12px;top:53px;width:28px">We back bold founders at the earliest stage, offering capital, counsel and a trusted network. Our partners stay close through every round, helping teams hire, sell and scale with focus and care.</div>
    <div class="fine" style="left:44px;top:53px;width:28px">We back bold founders at the earliest stage, offering capital, counsel and a trusted network. Our partners stay close through every round, helping teams hire, sell and scale with focus and care.</div>
    <div class="footer"><i></i>Northfield Ventures</div>
  </div>
  <span class="slot-num">8</span>
</div>

<div class="slot" style="left:414px;top:156px">
  <div class="slide">
    <div class="heading" style="left:12px;top:10px">Founder<br>Profile</div>
    <div class="heading-rule" style="left:12px;top:23px"></div>
    <div class="block-ink" style="left:140px;top:0;width:22px;height:28px"></div>
    <div class="photo" style="left:104px;top:10px;width:46px;height:66px" role="img" aria-label="Founder portrait"></div>
    <div class="fine" style="left:60px;top:29px;text-align:right;width:28px"><b>SAM KIT</b><br>Founder &amp; Managing Partner</div>
    <div class="col-divider" style="left:90px;top:28px;height:10px;background:var(--ink)"></div>
    <div class="fine" style="left:12px;top:56px;width:28px">We back bold founders at the earliest stage, offering capital, counsel and a trusted network. Our partners stay close through every round, helping teams hire and scale.</div>
    <div class="fine" style="left:44px;top:56px;width:28px">We back bold founders at the earliest stage, offering capital, counsel and a trusted network. Our partners stay close through every round, helping teams hire and scale.</div>
    <div class="footer"><i></i>Northfield Ventures</div>
  </div>
  <span class="slot-num">9</span>
</div>

<div class="slot" style="left:608px;top:156px">
  <div class="slide" style="background:var(--mist)">
    <div class="heading" style="left:12px;top:10px">Founder<br>Profile</div>
    <div class="heading-rule" style="left:12px;top:23px"></div>
    <div class="block-ink" style="left:140px;top:0;width:22px;height:28px"></div>
    <div class="photo" style="left:104px;top:10px;width:46px;height:66px;background:#f0f0f0" role="img" aria-label="Founder portrait"></div>
    <div class="fine" style="left:60px;top:29px;text-align:right;width:28px"><b>SAM KIT</b><br>Founder &amp; Managing Partner</div>
    <div class="col-divider" style="left:90px;top:28px;height:10px;background:var(--ink)"></div>
    <div class="fine" style="left:12px;top:56px;width:28px">We back bold founders at the earliest stage, offering capital, counsel and a trusted network. Our partners stay close through every round, helping teams hire and scale.</div>
    <div class="fine" style="left:44px;top:56px;width:28px">We back bold founders at the earliest stage, offering capital, counsel and a trusted network. Our partners stay close through every round, helping teams hire and scale.</div>
    <div class="footer"><i></i>Northfield Ventures</div>
  </div>
  <span class="slot-num">10</span>
</div>

<div class="slot" style="left:803px;top:156px">
  <div class="slide">
    <div class="block-ink" style="left:0;top:0;width:50px;height:92px"></div>
    <div class="block-ink" style="left:140px;top:0;width:22px;height:24px"></div>
    <div class="heading" style="left:10px;top:26px;color:var(--paper)">Our<br>Story</div>
    <div class="heading-rule" style="left:10px;top:39px;color:var(--paper)"></div>
    <div class="photo" style="left:58px;top:12px;width:92px;height:52px" role="img" aria-label="Company story video still"></div>
    <svg class="icon" style="left:100px;top:34px" width="6" height="8" viewBox="0 0 6 8"><path d="M1 1 L5 4 L1 7 Z" fill="none" stroke="#8a8a8a" stroke-width=".6"/></svg>
    <div class="abs" style="left:62px;top:58px;width:84px;height:.6px;background:#8a8a8a"></div>
    <div class="block-ink" style="left:58px;top:64px;width:92px;height:10px;background:#3a3a3a"></div>
    <div class="fine" style="left:61px;top:67px;width:86px;color:var(--paper)">Watch how we partner with founders from first cheque to exit</div>
    <div class="fine" style="left:10px;top:74px;width:36px;color:var(--paper)">Capital, counsel and a trusted network built for first rounds and the years after.</div>
    <div class="footer" style="left:110px;color:var(--ink)"><i></i>Northfield</div>
  </div>
  <span class="slot-num">11</span>
</div>

<div class="slot" style="left:997px;top:156px">
  <div class="slide">
    <div class="heading" style="left:10px;top:14px">Our<br>Services</div>
    <div class="heading-rule" style="left:10px;top:27px"></div>
    <div class="block-mist" style="left:0;top:50px;width:74px;height:42px"></div>
    <div class="block-ink" style="left:74px;top:0;width:88px;height:92px"></div>
    <svg class="icon" style="left:86px;top:14px" width="5" height="8" viewBox="0 0 5 8"><rect x=".5" y=".5" width="4" height="7" rx=".6" fill="none" stroke="#fff" stroke-width=".6"/></svg>
    <div class="fine bold" style="left:94px;top:14px;font-size:2.6px;color:var(--paper)">Advisory</div>
    <div class="fine" style="left:94px;top:19px;width:60px;color:var(--paper)">Board-level guidance on strategy, hiring and fundraising for early teams.</div>
    <svg class="icon" style="left:86px;top:37px" width="6" height="6" viewBox="0 0 6 6"><circle cx="3" cy="3" r="2.4" fill="none" stroke="#fff" stroke-width=".6"/><circle cx="3" cy="3" r="1" fill="#fff"/></svg>
    <div class="fine bold" style="left:94px;top:37px;font-size:2.6px;color:var(--paper)">Planning</div>
    <div class="fine" style="left:94px;top:42px;width:60px;color:var(--paper)">Clear operating plans, runway models and milestones for each round.</div>
    <svg class="icon" style="left:86px;top:59px" width="6" height="7" viewBox="0 0 6 7"><path d="M.5 1h5v3.5L3 6.5.5 4.5z" fill="none" stroke="#fff" stroke-width=".6"/></svg>
    <div class="fine bold" style="left:94px;top:59px;font-size:2.6px;color:var(--paper)">Implementation</div>
    <div class="fine" style="left:94px;top:64px;width:60px;color:var(--paper)">Hands-on support to launch, sell and scale with a proven network.</div>
    <div class="footer" style="left:78px;color:var(--paper)"><i></i>Northfield</div>
  </div>
  <span class="slot-num">12</span>
</div>

<!-- Row 3 -->
<div class="slot" style="left:25px;top:295px">
  <div class="slide">
    <div class="heading center" style="top:8px">Our Team</div>
    <div class="col-divider" style="left:81px;top:20px;height:58px"></div>
    <div class="photo" style="left:14px;top:24px;width:22px;height:20px" role="img" aria-label="Team member portrait"></div>
    <div class="fine" style="left:39px;top:24px;width:38px"><b>SAM KIT</b> · Partner<br>Backs founders in fintech and software, with two decades of operating and board experience across early rounds.</div>
    <div class="photo" style="left:14px;top:52px;width:22px;height:20px" role="img" aria-label="Team member portrait"></div>
    <div class="fine" style="left:39px;top:52px;width:38px"><b>SAM KIT</b> · Partner<br>Backs founders in fintech and software, with two decades of operating and board experience across early rounds.</div>
    <div class="photo" style="left:88px;top:24px;width:22px;height:20px" role="img" aria-label="Team member portrait"></div>
    <div class="fine" style="left:113px;top:24px;width:38px"><b>SAM KIT</b> · Partner<br>Backs founders in fintech and software, with two decades of operating and board experience across early rounds.</div>
    <div class="photo" style="left:88px;top:52px;width:22px;height:20px" role="img" aria-label="Team member portrait"></div>
    <div class="fine" style="left:113px;top:52px;width:38px"><b>SAM KIT</b> · Partner<br>Backs founders in fintech and software, with two decades of operating and board experience across early rounds.</div>
    <div class="footer"><i></i>Northfield Ventures</div>
  </div>
  <span class="slot-num">13</span>
</div>

<div class="slot" style="left:220px;top:295px">
  <div class="slide">
    <div class="heading center" style="top:8px">Our Competencies</div>
    <div class="block-fog" style="left:0;top:18px;width:162px;height:74px"></div>
    <svg class="icon" style="left:25px;top:22px" width="7" height="7" viewBox="0 0 7 7"><path d="M3.5 .6 6.4 6.4H.6z" fill="none" stroke="#000" stroke-width=".6"/></svg>
    <svg class="icon" style="left:64px;top:22px" width="7" height="7" viewBox="0 0 7 7"><path d="M4 .5 1.5 4h2L3 6.5 5.5 3h-2z" fill="none" stroke="#000" stroke-width=".6"/></svg>
    <svg class="icon" style="left:103px;top:22px" width="7" height="7" viewBox="0 0 7 7"><circle cx="3.5" cy="3.5" r="2.8" fill="none" stroke="#000" stroke-width=".6"/><path d="M3.5 3.5 5 2" stroke="#000" stroke-width=".6"/></svg>
    <svg class="icon" style="left:142px;top:22px" width="7" height="7" viewBox="0 0 7 7"><path d="M1 6 6 1M4 1h2v2" fill="none" stroke="#000" stroke-width=".6"/></svg>
    <div class="col-divider" style="left:48px;top:30px;height:46px"></div>
    <div class="col-divider" style="left:87px;top:30px;height:46px"></div>
    <div class="col-divider" style="left:126px;top:30px;height:46px"></div>
    <div class="fine" style="left:12px;top:32px;width:33px;text-align:center"><b>STRATEGY</b><br>Sharp market theses that guide where we invest, shaped with founders and tested against real customer demand.</div>
    <div class="fine" style="left:51px;top:32px;width:33px;text-align:center"><b>SOURCING</b><br>Sharp market theses that guide where we invest, shaped with founders and tested against real customer demand.</div>
    <div class="fine" style="left:90px;top:32px;width:33px;text-align:center"><b>DILIGENCE</b><br>Sharp market theses that guide where we invest, shaped with founders and tested against real customer demand.</div>
    <div class="fine" style="left:129px;top:32px;width:30px;text-align:center"><b>SCALING</b><br>Sharp market theses that guide where we invest, shaped with founders and tested against real customer demand.</div>
    <div class="footer"><i></i>Northfield Ventures</div>
  </div>
  <span class="slot-num">14</span>
</div>

<div class="slot" style="left:414px;top:295px">
  <div class="slide">
    <div class="block-mist" style="left:0;top:0;width:162px;height:20px"></div>
    <div class="heading center" style="top:24px">Our Process</div>
    <div class="col-divider" style="left:48px;top:36px;height:50px"></div>
    <div class="col-divider" style="left:87px;top:36px;height:50px"></div>
    <div class="col-divider" style="left:126px;top:36px;height:50px"></div>
    <div class="fine" style="left:12px;top:36px;width:33px;text-align:center"><b>DISCOVER</b><br>We meet teams early, learn the problem they solve and map the market, the risks and the path to the next round.</div>
    <div class="fine" style="left:51px;top:36px;width:33px;text-align:center"><b>ASSESS</b><br>We meet teams early, learn the problem they solve and map the market, the risks and the path to the next round.</div>
    <div class="fine" style="left:90px;top:36px;width:33px;text-align:center"><b>INVEST</b><br>We meet teams early, learn the problem they solve and map the market, the risks and the path to the next round.</div>
    <div class="fine" style="left:129px;top:36px;width:30px;text-align:center"><b>GROW</b><br>We meet teams early, learn the problem they solve and map the market, the risks and the path to the next round.</div>
    <svg class="icon" style="left:26px;top:80px" width="6" height="7" viewBox="0 0 6 7"><path d="M3.5.5 1 4h2l-.5 2.5L5 3H3z" fill="none" stroke="#000" stroke-width=".6"/></svg>
    <svg class="icon" style="left:65px;top:80px" width="6" height="7" viewBox="0 0 6 7"><path d="M3.5.5 1 4h2l-.5 2.5L5 3H3z" fill="none" stroke="#000" stroke-width=".6"/></svg>
    <svg class="icon" style="left:104px;top:80px" width="7" height="7" viewBox="0 0 7 7"><circle cx="3.5" cy="3.5" r="2.6" fill="none" stroke="#000" stroke-width=".6"/></svg>
    <svg class="icon" style="left:142px;top:80px" width="7" height="7" viewBox="0 0 7 7"><path d="M1 5.5 3.5 1 6 5.5z" fill="none" stroke="#000" stroke-width=".6"/></svg>
  </div>
  <span class="slot-num">15</span>
</div>

<div class="slot" style="left:608px;top:295px">
  <div class="slide">
    <div class="heading center" style="top:20px">Our Process</div>
    <div class="block-fog" style="left:0;top:30px;width:162px;height:62px"></div>
    <div class="col-divider" style="left:48px;top:34px;height:52px"></div>
    <div class="col-divider" style="left:87px;top:34px;height:52px"></div>
    <div class="col-divider" style="left:126px;top:34px;height:52px"></div>
    <div class="fine" style="left:12px;top:35px;width:33px;text-align:center"><b>DISCOVER</b><br>We meet teams early, learn the problem they solve and map the market, the risks and the path to the next round.</div>
    <div class="fine" style="left:51px;top:35px;width:33px;text-align:center"><b>ASSESS</b><br>We meet teams early, learn the problem they solve and map the market, the risks and the path to the next round.</div>
    <div class="fine" style="left:90px;top:35px;width:33px;text-align:center"><b>INVEST</b><br>We meet teams early, learn the problem they solve and map the market, the risks and the path to the next round.</div>
    <div class="fine" style="left:129px;top:35px;width:30px;text-align:center"><b>GROW</b><br>We meet teams early, learn the problem they solve and map the market, the risks and the path to the next round.</div>
    <svg class="icon" style="left:26px;top:78px" width="6" height="7" viewBox="0 0 6 7"><circle cx="3" cy="3.5" r="2.4" fill="none" stroke="#000" stroke-width=".6"/></svg>
    <svg class="icon" style="left:65px;top:78px" width="6" height="7" viewBox="0 0 6 7"><path d="M3.5.5 1 4h2l-.5 2.5L5 3H3z" fill="none" stroke="#000" stroke-width=".6"/></svg>
    <svg class="icon" style="left:104px;top:78px" width="7" height="7" viewBox="0 0 7 7"><circle cx="3.5" cy="3.5" r="2.6" fill="none" stroke="#000" stroke-width=".6"/></svg>
    <svg class="icon" style="left:142px;top:78px" width="7" height="7" viewBox="0 0 7 7"><path d="M1 5.5 3.5 1 6 5.5z" fill="none" stroke="#000" stroke-width=".6"/></svg>
  </div>
  <span class="slot-num">16</span>
</div>

<div class="slot" style="left:803px;top:295px">
  <div class="slide">
    <div class="block-ink" style="left:0;top:0;width:30px;height:18px"></div>
    <div class="photo" style="left:12px;top:10px;width:108px;height:74px" role="img" aria-label="Full-bleed feature photograph"></div>
    <div class="block-ink" style="left:120px;top:0;width:42px;height:92px"></div>
    <div class="heading" style="left:126px;top:18px;color:var(--paper)">Full<br>Picture<br>Slide</div>
    <div class="heading-rule" style="left:126px;top:35px;color:var(--paper)"></div>
    <div class="fine" style="left:126px;top:56px;width:32px;color:var(--paper)">Capital, counsel and a trusted network built for first rounds, with partners who stay close as teams grow.</div>
  </div>
  <span class="slot-num">17</span>
</div>

<div class="slot" style="left:997px;top:295px">
  <div class="slide">
    <div class="heading center" style="top:24px">Our Clients</div>
    <div class="client-box" style="left:14px;top:36px"></div><div class="client-box" style="left:50px;top:36px"></div><div class="client-box" style="left:86px;top:36px"></div><div class="client-box" style="left:122px;top:36px"></div>
    <div class="client-box" style="left:14px;top:45px"></div><div class="client-box" style="left:50px;top:45px"></div><div class="client-box" style="left:86px;top:45px"></div><div class="client-box" style="left:122px;top:45px"></div>
    <div class="client-box" style="left:14px;top:54px"></div><div class="client-box" style="left:50px;top:54px"></div><div class="client-box" style="left:86px;top:54px"></div><div class="client-box" style="left:122px;top:54px"></div>
    <div class="client-box" style="left:32px;top:66px"></div><div class="client-box" style="left:68px;top:66px"></div><div class="client-box" style="left:104px;top:66px"></div>
  </div>
  <span class="slot-num">18</span>
</div>

<!-- Row 4 -->
<div class="slot" style="left:25px;top:435px">
  <div class="slide">
    <div class="heading" style="left:10px;top:10px">Case<br>Study</div>
    <div class="heading-rule" style="left:10px;top:23px"></div>
    <div class="photo" style="left:80px;top:0;width:82px;height:30px" role="img" aria-label="Portfolio company photograph"></div>
    <div class="block-ink" style="left:0;top:36px;width:74px;height:56px"></div>
    <div class="fine bold" style="left:6px;top:42px;font-size:2.6px;color:var(--paper)">Seed round</div>
    <div class="fine" style="left:6px;top:48px;width:62px;color:var(--paper)">We led the seed round for a payments start-up with three founders and a working product, then helped them hire their first sales team and close a strong Series A within eighteen months.</div>
    <div class="fine" style="left:6px;top:72px;width:62px;color:var(--paper)"><b>$2.4M</b> raised · <b>18</b> months · <b>4x</b> revenue</div>
    <div class="fine" style="left:82px;top:33px;width:36px">We back bold founders at the earliest stage, offering capital, counsel and a trusted network. Our partners stay close through every round, helping teams hire, sell and scale with focus and care. Each plan is built with the team.</div>
    <div class="abs" style="left:122px;top:52px;width:34px;height:4px;border:.5px solid #000"></div>
    <div class="abs" style="left:122px;top:58px;width:34px;height:4px;border:.5px solid #000"></div>
    <div class="abs" style="left:122px;top:64px;width:34px;height:4px;border:.5px solid #000"></div>
    <div class="abs" style="left:122px;top:70px;width:34px;height:4px;border:.5px solid #000"></div>
    <div class="footer" style="left:78px"><i></i>Northfield Ventures</div>
  </div>
  <span class="slot-num">19</span>
</div>

<div class="slot" style="left:220px;top:435px">
  <div class="slide dark">
    <div class="block-paper" style="left:80px;top:0;width:82px;height:92px"></div>
    <div class="heading" style="left:12px;top:36px">Client<br>Feedback</div>
    <div class="heading-rule" style="left:12px;top:49px"></div>
    <div class="block-fog" style="left:54px;top:16px;width:96px;height:60px"></div>
    <div class="photo" style="left:96px;top:22px;width:12px;height:12px" role="img" aria-label="Client headshot"></div>
    <div class="fine" style="left:60px;top:40px;width:84px;text-align:center;color:#222">“Northfield backed us before anyone else would, and their partners were in the room for every hard decision that followed.”</div>
    <div class="fine bold" style="left:60px;top:50px;width:84px;text-align:center;color:#222">Sam Kit, Founder</div>
    <div class="footer" style="left:84px;color:var(--ink)"><i></i>Northfield Ventures</div>
  </div>
  <span class="slot-num">20</span>
</div>

<div class="slot" style="left:414px;top:435px">
  <div class="slide">
    <div class="heading" style="left:12px;top:14px">Thank<br>You</div>
    <div class="fine bold" style="left:12px;top:32px;letter-spacing:.1em">PRESENTATION TITLE</div>
    <div class="fine bold" style="left:12px;top:82px">MAY 2024</div>
    <div class="brand" style="left:80px;top:74px;font-size:2px"><span class="brand-square" style="width:4px;height:4px"></span>Northfield</div>
    <div class="fine" style="left:112px;top:73px;width:36px;font-size:1.6px">12 Harbour Lane, Suite 4<br>hello@northfield.vc<br>+1 555 0142</div>
  </div>
  <span class="slot-num">21</span>
</div>

<div class="slot" style="left:608px;top:435px">
  <div class="slide dark">
    <div class="heading" style="left:12px;top:14px">Thank<br>You</div>
    <div class="fine bold" style="left:12px;top:32px;letter-spacing:.1em">PRESENTATION TITLE</div>
    <div class="fine bold" style="left:12px;top:82px">MAY 2024</div>
    <div class="brand" style="left:80px;top:74px;font-size:2px"><span class="brand-square" style="width:4px;height:4px"></span>Northfield</div>
    <div class="fine" style="left:112px;top:73px;width:36px;font-size:1.6px">12 Harbour Lane, Suite 4<br>hello@northfield.vc<br>+1 555 0142</div>
  </div>
  <span class="slot-num">22</span>
</div>

</body>
</html>
```